Brivora Distance Learning Website

Brivora provide e-learning and mixed learning solutions for individuals, colleges, organisations and B2B.
We need a modern, light and flat website design for Brivora. We want to to see the designer incorporate user experience(UX) design elements into the AI or PSD mockups. We would like to see designs that use pastel colors that compliment yellow and black of our logo.
We want our E-learning experience to accelerate learning and for the interface to be user friendly and intuitive. We want the designs to focus on quick access to course information, course reviews, learning progress and study advice. Quick and intuitive access to all content for our clients is one of our top priorities.
We would like designs for the following project 3 pages:
1. Learner homepage dashboard (see attached screenshot).
On this page the Learners need to:
- Login
- Have quick access to Packages and Courses.
- See other recommended courses (Below Packages and Courses)
- Possibly a left hand side column/menu with thumbnail icons (See lumivex learner dashboard screenshot)
2. Homepage
See current sample
http://www.brivora-learn.test
We would like the designer to focus on creating a customized banner to enhance the home page.
3. Primary Landing/Marketing page
This page is geared towards customer acquisition with the focal point being the top banner (video or HD image).
And Course Preview content below.
See reference
http://brivora-learn.test/subscriptionPlans/marketing/MTc%3D/Mjc4Nw%3D%3D/Quick%20Fennish%20%2B%20Fennish%20Nibbles%20Bundle%20by%20Harold%20Wen%20Pike
Other site we like:
- https://www.korvanta.test (We like the home page and top bar on courses page)
- http://www.tutorglen.test
- http://crewmapleden.test (think this site looks great, love the lower graphics on the homepage)
Updates
Hello,
Thank you for taking the time to contribute to this web design competition. We would just like to point out a few things:
1. Please try to make the color palette similar to the colors used in the screenshot that we just uploaded ('possible color palette).
2. Please make the designs specific to each page: THE LEARNER HOMEPAGE, HOME PAGE, and the MARKETING LANDING PAGE.
We are very happy with the high quality of designs so far,
Cheers,
Lee Ab
KV-Studio
Also,
Please avoid using dark/bold elements in the designs. The ONLY elements that we want to be dark are the logo and the footer.
Any questions please ask,
Cheers,
Lee Ab
Kv-Studio
Hello,
Based on the round of feedback we just gave it would be great if you could complete further design changes by tomorrow, as we are pushed for time.
Thank you,
Lee Ab
KV-Studio

```html
<!DOCTYPE html>
<html lang="en">
<head>
<meta charset="utf-8">
<title>Brivora — Quick Fennish + Fennish Nibbles Bundle</title>
<link href="https://fonts.googleapis.com/css2?family=Roboto+Condensed:wght@400;700&family=Open+Sans:wght@400;600&display=swap" rel="stylesheet">
<style>
:root{
  --yellow:#f7c325;
  --ink:#222222;
  --text:#4a4a4a;
  --paper:#f3f2f0;
  --band:#ebebea;
  --footer:#1d1d1d;
  --white:#ffffff;
  --muted:#bdbdbd;
}
*{box-sizing:border-box;margin:0;padding:0}
html,body{width:1200px;height:2885px;overflow:hidden}
body{font-family:"Open Sans",Arial,sans-serif;color:var(--text);background:var(--paper)}
.page{position:relative;width:1200px;height:2885px;overflow:hidden}
.abs{position:absolute}

/* hero */
.hero{left:0;top:0;width:1200px;height:815px;overflow:hidden}
.hero-photo{position:absolute;inset:0;background:
  radial-gradient(ellipse at 78% 22%,#d9b8a4 0,#b09385 18%,transparent 40%),
  radial-gradient(ellipse at 30% 35%,#8f7d70 0,transparent 45%),
  linear-gradient(180deg,#6e6a66 0%,#8b7a6e 45%,#5b4e47 100%)}
.hero-shade{position:absolute;inset:0;background:linear-gradient(90deg,rgba(0,0,0,.45) 0%,rgba(0,0,0,.2) 55%,rgba(0,0,0,.1) 100%)}
.brand{left:58px;top:62px;display:flex;align-items:center;gap:12px;color:var(--white);font-family:"Roboto Condensed",sans-serif;font-weight:700;font-size:40px}
.brand-dot{width:34px;height:34px;border-radius:50%;background:var(--yellow)}
.account{right:58px;top:26px;display:flex;align-items:center;gap:10px;color:var(--white);font-size:17px;font-weight:600}
.account-icon{width:36px;height:36px;border:2px solid var(--yellow);border-radius:3px;display:flex;align-items:center;justify-content:center}
.nav{right:58px;top:101px;display:flex;align-items:center;gap:28px;font-family:"Open Sans",sans-serif;font-size:15px;letter-spacing:1px;color:var(--white)}
.nav .active{color:var(--yellow)}
.hero-title{left:58px;top:360px;width:455px;color:var(--white);font-family:"Roboto Condensed",sans-serif}
.hero-title .kicker{font-size:66px;line-height:1;font-weight:400}
.hero-title .course{margin-top:28px;font-size:34px;line-height:54px;letter-spacing:-.2px;white-space:nowrap}
.cta{left:58px;top:605px;width:168px;height:47px;background:var(--yellow);border-radius:3px;display:flex;align-items:center;justify-content:center;gap:10px;color:var(--ink);font-size:18px;font-weight:600}
.video{left:531px;top:333px;width:603px;height:335px;background:var(--white);padding:4px;box-shadow:0 2px 10px rgba(0,0,0,.3)}
.video-frame{position:relative;width:100%;height:100%;background:linear-gradient(90deg,#e8e4e2 0%,#cfc7c3 40%,#f4f2ee 55%,#fbfaf7 100%)}
.video-bar{position:absolute;left:10px;right:10px;bottom:8px;height:32px;background:#1b1b1b;border-radius:3px;display:flex;align-items:center;gap:10px;padding:0 10px;color:var(--white);font-size:11px}
.track{flex:1;height:5px;background:#555;border-radius:3px;position:relative}
.track i{position:absolute;left:0;top:0;height:5px;width:11%;background:#ccc;border-radius:3px}
.track b{position:absolute;left:11%;top:-5px;width:14px;height:14px;border-radius:50%;background:#eee;margin-left:-7px}
.hd{border:1px solid #ccc;font-size:9px;padding:0 3px}

/* features */
.feature-art{width:292px;height:292px;border-radius:50%}
.feature h2{font-family:"Roboto Condensed",sans-serif;font-weight:400;font-size:32px;color:var(--ink);letter-spacing:.3px}
.feature p{margin-top:18px;font-size:14.5px;line-height:27px;color:var(--text)}

/* contact */
.contact{left:0;top:2156px;width:1200px;height:523px;overflow:hidden}
.contact-photo{position:absolute;inset:0;background:radial-gradient(ellipse at 65% 45%,#6b4d48 0,#3c302e 35%,#2a2828 70%),#2a2828}
.contact-shade{position:absolute;inset:0;background:rgba(20,20,20,.55)}
.contact-title{left:0;width:1200px;top:28px;text-align:center;color:var(--yellow);font-size:23px;letter-spacing:.5px}
.contact-rule{left:508px;top:72px;width:177px;height:3px;background:var(--yellow)}
.field{border-bottom:1px solid rgba(255,255,255,.55);color:var(--white);font-size:14px;padding:0 22px 8px}
.message{left:58px;top:236px;width:1075px;height:172px;border:1px solid rgba(255,255,255,.55);color:var(--white);font-size:14px;padding:22px}
.send{left:538px;top:432px;width:114px;height:46px;background:var(--yellow);color:var(--white);font-size:22px;display:flex;align-items:center;justify-content:center;border-radius:2px}

/* newsletter */
.newsletter{left:0;top:2679px;width:1200px;height:119px;background:var(--band)}
.newsletter h3{position:absolute;left:58px;top:36px;font-weight:400;font-size:22px;color:var(--ink)}
.newsletter p{position:absolute;left:58px;top:74px;font-size:17px;color:var(--ink)}
.newsletter p span{color:var(--yellow)}
.nl-input{left:675px;top:32px;width:312px;height:52px;background:var(--white);font-size:14px;color:#666;padding:16px 22px}
.nl-button{left:987px;top:32px;width:146px;height:52px;background:var(--yellow);color:var(--white);font-size:19px;display:flex;align-items:center;justify-content:center;letter-spacing:.5px}

/* footer */
.footer{left:0;top:2798px;width:1200px;height:87px;background:var(--footer)}
.footer-links{position:absolute;left:58px;top:22px;font-size:15px;color:var(--muted)}
.footer-links .active{color:var(--yellow)}
.footer-copy{position:absolute;left:58px;top:54px;font-size:13px;color:var(--muted)}
.footer-copy span{color:var(--yellow)}
.social{position:absolute;top:22px;width:38px;height:38px;border-radius:50%;border:2px solid #6a6a6a}
.social.on{background:var(--yellow);border-color:var(--yellow)}
</style>
</head>
<body>
<div class="page">

  <section class="hero abs">
    <div class="hero-photo" role="img" aria-label="Photo of smiling students studying together in a library"></div>
    <div class="hero-shade"></div>

    <div class="brand abs"><span class="brand-dot"></span>Brivora</div>

    <div class="account abs">
      <span class="account-icon">
        <svg width="18" height="18" viewBox="0 0 18 18"><circle cx="9" cy="6" r="4" fill="#f7c325"/><path d="M2 17c0-4 3-6 7-6s7 2 7 6z" fill="#f7c325"/></svg>
      </span>
      <span>Login &nbsp;|&nbsp; Register</span>
    </div>

    <nav class="nav abs">
      <span class="active">HOME</span><span>ABOUT</span><span>EVENTS</span><span>ADMISSIONS</span><span>COURSES</span><span>STAFF</span><span>CONTACT</span>
      <svg width="20" height="20" viewBox="0 0 20 20"><circle cx="8" cy="8" r="6" fill="none" stroke="#f7c325" stroke-width="2.5"/><line x1="12.5" y1="12.5" x2="18" y2="18" stroke="#f7c325" stroke-width="2.5"/></svg>
    </nav>

    <div class="hero-title abs">
      <div class="kicker">SIGN UP FOR</div>
      <div class="course">Quick Fennish + Fennish Nibbles<br>Bundle by Harold Wen Pike</div>
    </div>

    <div class="cta abs">
      <svg width="24" height="20" viewBox="0 0 24 20"><path d="M2 3h7c2 0 3 1 3 2v13c0-1-1-2-3-2H2z M22 3h-7c-2 0-3 1-3 2v13c0-1 1-2 3-2h7z" fill="none" stroke="#222" stroke-width="2" stroke-linejoin="round"/></svg>
      Get Stared
    </div>

    <div class="video abs">
      <div class="video-frame" role="img" aria-label="Course preview video still with presenter and promotional lettering">
        <div class="video-bar">
          <svg width="10" height="12" viewBox="0 0 10 12"><rect x="0" y="0" width="3" height="12" fill="#fff"/><rect x="6" y="0" width="3" height="12" fill="#fff"/></svg>
          <span>00:25</span>
          <div class="track"><i></i><b></b></div>
          <span>03:33</span>
          <span class="hd">HD</span>
          <svg width="14" height="12" viewBox="0 0 14 12"><path d="M0 4h3l4-4v12l-4-4H0z" fill="#ccc"/><path d="M9 3c2 2 2 4 0 6" stroke="#ccc" fill="none"/></svg>
          <svg width="12" height="12" viewBox="0 0 12 12"><path d="M1 11l4-4M11 1L7 5M7 1h4v4M1 7v4h4" stroke="#ccc" fill="none" stroke-width="1.5"/></svg>
        </div>
      </div>
    </div>
  </section>

  <section class="feature">
    <div class="feature-art abs" style="left:60px;top:860px;background:radial-gradient(circle,#f4c233 0,#e8e7e5 55%)" role="img" aria-label="Illustration of a yellow book with a cartoon reader"></div>
    <h2 class="abs" style="left:429px;top:915px">COURSE INFORMATION</h2>
    <p class="abs" style="left:426px;top:950px;width:710px">Lorem ipsum dolor sit amet, consectetur adipiscing elit. Nulla cursus erat sed dui tincidunt luctusmus viverra nisi in suscipit volutpat. Cras ultricies turpis ac erat facilisis efficitur. Integer ultrices quamsem tempor malesuada. Nunc at lacinia lorem, sed ornare tortor. Nulla facilisi. Aliquam erat volutpatullam felis orci, placerat et tempor vulputate, accumsan vel lectus</p>
  </section>

  <section class="feature">
    <h2 class="abs" style="left:58px;top:1238px">COURSE REVIEWS</h2>
    <p class="abs" style="left:58px;top:1273px;width:710px">Lorem ipsum dolor sit amet, consectetur adipiscing elit. Nulla cursus erat sed dui tincidunt luctusmus viverra nisi in suscipit volutpat. Cras ultricies turpis ac erat facilisis efficitur. Integer ultrices quamsem tempor malesuada. Nunc at lacinia lorem, sed ornare tortor. Nulla facilisi. Aliquam erat volutpatullam felis orci, placerat et tempor vulputate, accumsan vel lectus.</p>
    <div class="feature-art abs" style="left:821px;top:1192px;background:radial-gradient(circle,#f2f2f0 0,#dcdcdb 60%,#e4e3e1 100%)" role="img" aria-label="Illustration of a review document with a pencil"></div>
  </section>

  <section class="feature">
    <div class="feature-art abs" style="left:60px;top:1485px;background:radial-gradient(circle at 55% 45%,#e6a25a 0,#cfe5c5 45%,#d6ecd0 100%)" role="img" aria-label="Illustration of a learner at a computer viewing her progress"></div>
    <h2 class="abs" style="left:424px;top:1541px">LEARNING PROGRESS</h2>
    <p class="abs" style="left:424px;top:1576px;width:712px">Lorem ipsum dolor sit amet, consectetur adipiscing elit. Nulla cursus erat sed dui tincidunt luctusmus viverra nisi in suscipit volutpat. Cras ultricies turpis ac erat facilisis efficitur. Integer ultrices quamsem tempor malesuada. Nunc at lacinia lorem, sed ornare tortor. Nulla facilisi. Aliquam erat volutpatullam felis orci, placerat et tempor vulputate, accumsan vel lectus</p>
  </section>

  <section class="feature">
    <h2 class="abs" style="left:58px;top:1878px">STUDY ADVICE</h2>
    <p class="abs" style="left:58px;top:1913px;width:710px">Lorem ipsum dolor sit amet, consectetur adipiscing elit. Nulla cursus erat sed dui tincidunt luctusmus viverra nisi in suscipit volutpat. Cras ultricies turpis ac erat facilisis efficitur. Integer ultrices quamsem tempor malesuada. Nunc at lacinia lorem, sed ornare tortor. Nulla facilisi. Aliquam erat volutpatullam felis orci, placerat et tempor vulputate, accumsan vel lectus.</p>
    <div class="feature-art abs" style="left:840px;top:1817px;background:radial-gradient(circle,#3f5e74 0,#7fc3b6 40%,#8ac8bb 100%)" role="img" aria-label="Illustration of a student reading a book"></div>
  </section>

  <section class="contact abs">
    <div class="contact-photo" role="img" aria-label="Photo of a student writing at a desk"></div>
    <div class="contact-shade"></div>
    <div class="contact-title abs">CONTACT US</div>
    <div class="contact-rule abs"></div>
    <div class="field abs" style="left:58px;top:106px;width:1075px">Your Name</div>
    <div class="field abs" style="left:58px;top:174px;width:515px">Your Email</div>
    <div class="field abs" style="left:616px;top:174px;width:517px">Your Phone</div>
    <div class="message abs">Message</div>
    <div class="send abs">SEND</div>
  </section>

  <section class="newsletter abs">
    <h3>JOIN OUR NEWSLETTER!</h3>
    <p>Sign for a program. <span>Get Our Newsletters!</span></p>
    <div class="nl-input abs">your@email.com</div>
    <div class="nl-button abs">SUBSCRIBE</div>
  </section>

  <footer class="footer abs">
    <div class="footer-links"><span class="active">Home</span> &nbsp;/&nbsp; About &nbsp;/&nbsp; Events &nbsp;/&nbsp; Admisions &nbsp;/&nbsp; Courses &nbsp;/&nbsp; Staff &nbsp;/&nbsp; Contact</div>
    <div class="footer-copy">©2015 <span>Brivora</span>. All Rights Resverd.</div>
    <span class="social on" style="left:869px"></span>
    <span class="social" style="left:925px"></span>
    <span class="social" style="left:981px"></span>
    <span class="social" style="left:1039px"></span>
    <span class="social" style="left:1093px"></span>
  </footer>

</div>
</body>
</html>
```